Zanquorra Business Card Design

Zanquorra is a small and new restaurant/ bar location in Hong Kong. The name "Djibouti" derives from an African country. There is no specific reason behind other than the fact, that the bar is somewhat inspired by African elements (only inspired but not purely based on African cuisine etc.).

The bar is somewhat a fusion of African, Mediterranean and Oriental (Old French Vietnam) elements.

However, it is very imperative to stress, that the overall look and feel of Zanquorra is a very high end cocktail lounge/ bar location. The bar is tucked away in a hidden alley, so people will have to know about it. The idea is to send the consumer off in an Escape or hidden remote location where they are at ease in a hip, stylish and trendy environment.

The card needs to feel high-end.

Final logo artwork has been attached and also pictures of the bar/ restaurant itself. The logo ie monkey head cannot be modified. However, the background color and the color of the type "ZANQUORRA" can be changed.

The following details need to fit onto the business card. Of course they can be arranged to your liking:

LOGO

Colin Vey
Partner

+852 97035164
xxx@zanquorra.com
www.zanquorra.com
7C, Brennick Road, Wan Chai, Hong Kong

```html
<!DOCTYPE html>
<html lang="en">
<head>
<meta charset="utf-8">
<title>Zanquorra Business Card</title>
<link href="https://fonts.googleapis.com/css2?family=Questrial&display=swap" rel="stylesheet">
<style>
  :root {
    --backdrop: #e9e4dc;
    --card: #ffffff;
    --ink: #2a2420;
    --accent: #8a6a3c;
    --shadow: rgba(40, 30, 20, 0.22);
  }
  * { margin: 0; padding: 0; box-sizing: border-box; }
  html, body {
    width: 1200px;
    height: 1023px;
    overflow: hidden;
    background: var(--backdrop);
    font-family: "Questrial", "Century Gothic", sans-serif;
    color: var(--ink);
  }
  .stage {
    width: 1200px;
    height: 1023px;
    display: flex;
    align-items: center;
    justify-content: center;
    gap: 90px;
  }
  .card {
    width: 400px;
    height: 680px;
    background: var(--card);
    box-shadow: 0 14px 34px var(--shadow);
    display: flex;
    flex-direction: column;
    align-items: center;
  }
  .card--front { justify-content: center; }
  .brand-mark {
    width: 300px;
    height: 300px;
    border: 5px solid var(--ink);
    border-radius: 50%;
  }
  .card--back { padding-top: 70px; }
  .card--back .brand-mark {
    width: 230px;
    height: 230px;
    border-width: 4px;
  }
  .brand-name {
    margin-top: 26px;
    font-size: 50px;
    letter-spacing: 2px;
    color: var(--ink);
  }
  .card--front .brand-name { margin-top: 40px; font-size: 46px; }
  .person-name {
    margin-top: 10px;
    font-size: 30px;
    letter-spacing: 1px;
  }
  .person-role {
    font-size: 17px;
    color: var(--accent);
  }
  .contact-list {
    list-style: none;
    margin-top: 34px;
    text-align: center;
    font-size: 20px;
    line-height: 1.35;
    color: var(--accent);
  }
  .contact-list .label { color: var(--ink); }
  .address {
    margin-top: 22px;
    text-align: center;
    font-size: 20px;
    line-height: 1.3;
    color: var(--accent);
    font-style: normal;
  }
</style>
</head>
<body>
  <main class="stage">
    <section class="card card--front">
      <div class="brand-mark"></div>
      <div class="brand-name">ZANQUORRA</div>
    </section>

    <section class="card card--back">
      <div class="brand-mark"></div>
      <div class="brand-name">ZANQUORRA</div>
      <div class="person-name">Colin Vey</div>
      <div class="person-role">Partner</div>
      <ul class="contact-list">
        <li><span class="label">[P]</span> +852 97035164</li>
        <li><span class="label">[E]</span> colinvey@zanquorra.com</li>
        <li><span class="label">[W]</span> www.zanquorra.com</li>
      </ul>
      <address class="address">7C, Brennick Road, Wan Chai,<br>Hong Kong</address>
    </section>
  </main>
</body>
</html>
```